Business Card for Lumina Nest

I need a very attractive business card as per the logo..

lumina nest is a centre providing services to pregnant women...

DR. Karim Haddadi

Consultant-  Maternal Fetal Medicine & Director of Lumina Nest Center

Kingdom of Saudi Arabia

Tel : +966 1 57 3 8164

Fax : +966 1 57 3 9275

khaddadi@luminest-example.com

www.luminanest-example.com

Target Market(s)

the target market is the pregnant women and women having issues with pregnancy or with babies

Industry/Entity Type

Business

Requirements
Must have
• the business card will be in English and Arabic..........one we finalize the design maybe on the back u can place Arabic..of in the front one side may be Arabic one side english

```html
<!DOCTYPE html>
<html lang="en">
<head>
<meta charset="utf-8">
<title>Lumina Nest – Business Card</title>
<link rel="stylesheet" href="https://fonts.googleapis.com/css2?family=Ubuntu:wght@300;400;700&display=swap">
<style>
  :root {
    --bg: #dcdcdc;
    --card: #ffffff;
    --teal: #6cc7b7;
    --teal-light: #bfe6df;
    --pink: #f4c1c6;
    --pink-light: #f9dde0;
    --pink-strong: #f3a0a9;
    --ink: #555b5f;
    --ink-dark: #3f4447;
    --white: #ffffff;
  }
  * { margin: 0; padding: 0; box-sizing: border-box; }
  html, body {
    width: 1200px; height: 1000px; overflow: hidden;
    background: var(--bg);
    font-family: "Ubuntu", sans-serif;
  }
  .stage {
    position: relative; width: 1200px; height: 1000px;
    display: flex; justify-content: center; align-items: center; gap: 90px;
  }
  .card {
    position: relative; width: 380px; height: 640px;
    background: var(--card); border-radius: 26px; overflow: hidden;
    box-shadow: 0 4px 14px rgba(0,0,0,0.12);
  }
  .card-bands { position: absolute; inset: 0; width: 100%; height: 100%; }

  /* Front */
  .front-brand {
    position: absolute; top: 70px; left: 0; right: 0;
    display: flex; align-items: center; justify-content: center; gap: 12px;
  }
  .brand-dot { width: 22px; height: 22px; border-radius: 50%; background: var(--teal); }
  .brand-name { font-size: 34px; font-weight: 400; color: var(--teal); letter-spacing: 0.5px; }
  .person {
    position: absolute; top: 150px; left: 40px; right: 40px; text-align: center;
    color: var(--ink);
  }
  .person-name { font-size: 22px; font-weight: 700; color: var(--ink-dark); }
  .person-role { font-size: 17px; font-weight: 300; margin-top: 4px; }
  .person-detail { font-size: 16px; font-weight: 300; line-height: 1.4; margin-top: 14px; }
  .contact {
    position: absolute; bottom: 46px; left: 40px; right: 40px; text-align: center;
    color: var(--white); font-size: 16px; font-weight: 300; line-height: 1.55;
  }
  .contact-web { font-weight: 700; font-size: 17px; }

  /* Back */
  .back-mark {
    position: absolute; top: 150px; left: 50%; transform: translateX(-50%);
    width: 150px; height: 150px; border-radius: 50%; background: var(--teal);
  }
  .back-name {
    position: absolute; top: 360px; left: 0; right: 0; text-align: center;
    font-size: 52px; font-weight: 400; color: var(--teal); letter-spacing: 0.5px;
  }
</style>
</head>
<body>
<main class="stage">

  <section class="card card-front">
    <svg class="card-bands" viewBox="0 0 380 640" preserveAspectRatio="none" aria-hidden="true">
      <path d="M230 0 H380 V185 C360 150 330 140 290 125 C255 110 240 60 230 0 Z" fill="var(--pink-light)"/>
      <path d="M270 0 H380 V170 C365 140 345 130 320 118 C290 100 275 55 270 0 Z" fill="var(--pink)"/>
      <path d="M0 400 C40 390 90 385 120 400 C150 418 160 500 170 640 H0 Z" fill="var(--teal-light)"/>
      <path d="M0 425 C30 410 70 405 100 420 C130 440 145 520 150 640 H380 V640 H0 Z" fill="var(--teal)"/>
      <path d="M0 640 V425 C30 410 70 405 100 420 C130 440 150 480 190 490 C260 505 330 500 380 520 V640 Z" fill="var(--teal)"/>
    </svg>

    <div class="front-brand">
      <span class="brand-dot"></span>
      <span class="brand-name">Lumina Nest</span>
    </div>

    <div class="person">
      <p class="person-name">Dr. Karim Haddadi</p>
      <p class="person-role">Consultant</p>
      <p class="person-detail">Maternal Fetal Medicine<br>&amp; Director of Lumina Nest Center<br>Kingdom of Saudi Arabia</p>
    </div>

    <div class="contact">
      <p>Tel : +966 1 57 3 8164</p>
      <p>Fax : +966 1 57 3 9275</p>
      <p>khaddadi@luminest-example.com</p>
      <p class="contact-web">www.luminanest-example.com</p>
    </div>
  </section>

  <section class="card card-back">
    <span class="back-mark"></span>
    <p class="back-name">Lumina Nest</p>
  </section>

</main>
</body>
</html>
```